Velmorra Design Group Business Card Design

We need a double-sided business card for our company Velmorra Design Group. Our slogan is "Simple Online Solutions." We are looking for a techy, cutting-edge but simple card that looks modern and sleek. We have a black logo attached and would prefer a lighter background to make our logo stand out. We like nice accents to make it pop out and make our clients remember our card.

On the back side, we just want our logo, slogan and website. Again, something very simple. Make the logo big on the back.

```html
<!DOCTYPE html>
<html lang="en">
<head>
<meta charset="utf-8">
<title>Velmorra Design Group – Business Card</title>
<link href="https://fonts.googleapis.com/css2?family=Exo+2:wght@400;700&family=Open+Sans:wght@400;600&display=swap" rel="stylesheet">
<style>
  :root {
    --yellow: #f6d800;
    --yellow-deep: #e2c200;
    --black: #111111;
    --ink: #1a1a1a;
    --backdrop: #d8d3ca;
    --card-w: 700px;
    --card-h: 400px;
  }
  * { box-sizing: border-box; margin: 0; padding: 0; }
  html, body {
    width: 1200px;
    height: 1000px;
    overflow: hidden;
    background: var(--backdrop);
    font-family: "Exo 2", sans-serif;
  }
  .card-sheet {
    position: relative;
    width: 1200px;
    height: 1000px;
  }
  .card {
    position: absolute;
    left: 250px;
    width: var(--card-w);
    height: var(--card-h);
    background: linear-gradient(135deg, var(--yellow) 0%, var(--yellow-deep) 100%);
    border-radius: 4px;
    overflow: hidden;
    box-shadow: 0 10px 28px rgba(0,0,0,0.25);
  }
  .card--front { top: 60px; }
  .card--back { top: 540px; }
  .card__shape {
    position: absolute;
    inset: 0;
    width: 100%;
    height: 100%;
  }
  .brand-name {
    position: absolute;
    color: var(--ink);
    font-weight: 400;
    white-space: nowrap;
    line-height: 1.2;
  }
  .card--front .brand-name {
    left: 40px;
    top: 56px;
    font-size: 38px;
  }
  .slogan {
    position: absolute;
    right: 40px;
    top: 248px;
    color: var(--yellow);
    font-size: 32px;
    font-weight: 400;
    white-space: nowrap;
    line-height: 1.2;
  }
  .card--front .website {
    position: absolute;
    right: 40px;
    top: 304px;
    color: var(--yellow);
    font-size: 22px;
    font-family: "Open Sans", sans-serif;
  }
  .card--back .brand-name {
    right: 40px;
    top: 36px;
    font-size: 30px;
  }
  .person {
    position: absolute;
    left: 360px;
    top: 232px;
    color: var(--yellow);
    line-height: 1.2;
  }
  .person__name {
    font-size: 30px;
    font-weight: 700;
  }
  .person__role {
    font-family: "Open Sans", sans-serif;
    font-size: 17px;
  }
  .contact-list {
    position: absolute;
    left: 44px;
    top: 176px;
    list-style: none;
    font-family: "Open Sans", sans-serif;
    font-size: 18px;
    color: var(--yellow);
  }
  .contact-list li {
    display: flex;
    align-items: center;
    gap: 14px;
    height: 40px;
  }
  .contact-list svg { width: 20px; height: 20px; flex: none; }
  .contact-list .divider {
    height: 18px;
  }
  .contact-list .divider span {
    display: block;
    width: 180px;
    height: 2px;
    background: var(--yellow);
  }
</style>
</head>
<body>
<main class="card-sheet">

  <section class="card card--front" aria-label="Business card, slogan side">
    <svg class="card__shape" viewBox="0 0 700 400" preserveAspectRatio="none" aria-hidden="true">
      <path d="M140 400 C 220 230, 430 90, 700 20 L700 400 Z" fill="var(--black)"/>
    </svg>
    <p class="brand-name">Velmorra Design Group</p>
    <p class="slogan">Simple Online Solutions</p>
    <p class="website">www.velmorra.ca</p>
  </section>

  <section class="card card--back" aria-label="Business card, contact side">
    <svg class="card__shape" viewBox="0 0 700 400" preserveAspectRatio="none" aria-hidden="true">
      <path d="M0 40 C 330 40, 620 200, 660 400 L0 400 Z" fill="var(--black)"/>
      <path d="M0 70 C 310 70, 585 215, 628 400" fill="none" stroke="var(--yellow)" stroke-width="4"/>
    </svg>
    <p class="brand-name">Velmorra Design Group</p>

    <ul class="contact-list">
      <li>
        <svg viewBox="0 0 20 20" aria-hidden="true"><path d="M10 1a6 6 0 0 0-6 6c0 4.5 6 12 6 12s6-7.5 6-12a6 6 0 0 0-6-6zm0 8.3A2.3 2.3 0 1 1 10 4.7a2.3 2.3 0 0 1 0 4.6z" fill="var(--yellow)"/></svg>
        <span>your address</span>
      </li>
      <li>
        <svg viewBox="0 0 20 20" aria-hidden="true"><path d="M5 2l3 4-2 2c1 2.5 3.5 5 6 6l2-2 4 3-2 3C9 18 2 11 2 4z" fill="var(--yellow)"/></svg>
        <span>123 456 789</span>
      </li>
      <li class="divider"><span></span></li>
      <li>
        <svg viewBox="0 0 20 20" aria-hidden="true"><rect x="2" y="4" width="16" height="12" fill="var(--yellow)"/><path d="M2 4l8 7 8-7" fill="none" stroke="var(--black)" stroke-width="1.5"/></svg>
        <span>yourname@velmorra.ca</span>
      </li>
      <li>
        <svg viewBox="0 0 20 20" aria-hidden="true"><circle cx="10" cy="10" r="8" fill="none" stroke="var(--yellow)" stroke-width="2"/><ellipse cx="10" cy="10" rx="3.5" ry="8" fill="none" stroke="var(--yellow)" stroke-width="1.5"/><path d="M2 10h16M3.5 6h13M3.5 14h13" stroke="var(--yellow)" stroke-width="1.2"/></svg>
        <span>www.velmorra.ca</span>
      </li>
    </ul>

    <div class="person">
      <p class="person__name">John Doe</p>
      <p class="person__role">your position</p>
    </div>
  </section>

</main>
</body>
</html>
```